Interior Design/Decor and Staging Website

Current website: www.marlowcrestinteriors.example but need something lighter and more appealing. Logo is also being changed. I would like a clean cut look, modern and professional. Would like a slideshow for portfolio pictures, social media icons and logos of where the work has been featured: VORNA, Nest Wares, Durrandel, Tobias Quill, Plaza Furnishings, etc.

Target Market(s)

interior design and interior decor clients, both local and international.

Industry/Entity Type

Home Improvement

Number of Pages Required

5+ page

Font styles to use
Sans Serif

Requirements
Nice to have
• Testimonial page and Dwellr reviews.

```html
<!DOCTYPE html>
<html lang="en">
<head>
<meta charset="utf-8">
<title>Marlow Crest Interiors</title>
<link href="https://fonts.googleapis.com/css2?family=Cinzel:wght@400;700&family=Open+Sans:wght@400;600&display=swap" rel="stylesheet">
<style>
:root{
  --gold:#c9a24a;
  --gold-light:#e3c988;
  --gold-btn:#c6a564;
  --header-top:#8d8d8d;
  --header-bottom:#6b6b6b;
  --text:#4a4a4a;
  --muted:#6f6f6f;
  --panel:#f1f1f1;
  --footer:#585858;
  --footer-bar:#4a4a4a;
  --white:#ffffff;
}
*{margin:0;padding:0;box-sizing:border-box}
html,body{width:1200px;height:2903px;overflow:hidden}
body{position:relative;background:var(--white);font-family:"Open Sans",Arial,sans-serif;color:var(--text)}
.abs{position:absolute}
.serif{font-family:"Cinzel",Georgia,serif}

/* header */
.site-header{left:0;top:0;width:1200px;height:155px;background:linear-gradient(var(--header-top),var(--header-bottom));border-top:5px solid var(--gold-light)}
.brand{left:100px;top:30px;display:flex;align-items:center;gap:14px}
.brand-mark{width:40px;height:40px;border:2px solid var(--gold-light)}
.brand-name{color:var(--gold-light);font-family:"Cinzel",Georgia,serif;font-size:27px;line-height:30px;letter-spacing:1px}
.social-top{right:100px;top:40px;display:flex;gap:14px}
.social-top span{width:38px;height:38px;border-radius:50%;background:linear-gradient(#9a9a9a,#5e5e5e);border:2px solid #bdbdbd;display:block}
.main-nav{right:98px;top:96px;display:flex;gap:50px;font-family:"Cinzel",Georgia,serif;font-size:14px;color:var(--white);letter-spacing:.5px}
.main-nav .active{color:var(--gold-light)}

/* hero */
.hero{left:0;top:155px;width:1200px;height:513px;background:linear-gradient(100deg,#d9d6d0 0%,#b9b2a6 30%,#8a6d52 60%,#e2ddd5 80%,#c6c0b6 100%)}
.hero-arrow{top:385px}
.hero-tag{left:588px;top:512px;display:flex;align-items:center;gap:14px;color:var(--white);font-family:"Cinzel",Georgia,serif;font-size:26px;line-height:28px}
.hero-tag .sq{width:34px;height:34px;border:2px solid var(--white)}

/* headings */
.section-title{left:0;width:1200px;text-align:center;color:var(--gold);font-family:"Cinzel",Georgia,serif;font-size:31px;letter-spacing:1px}

.welcome-text{left:160px;top:763px;width:880px;text-align:center;font-size:11.5px;line-height:25px;color:var(--text)}

/* services */
.services{left:0;top:955px;width:1200px;height:660px;background:linear-gradient(90deg,#e4e2dc,#f4f3ef 30%,#f0eee9 60%,#dcd8cf)}
.card{top:1200px;width:305px;height:352px;background:var(--white);box-shadow:0 6px 14px rgba(0,0,0,.18);text-align:center;padding:0 16px}
.card h3{margin-top:98px;font-family:"Cinzel",Georgia,serif;font-weight:400;font-size:18px;color:#333;letter-spacing:.5px}
.card p{margin-top:8px;font-size:12px;line-height:18px;color:#555}
.btn{position:absolute;left:102px;top:295px;width:103px;height:37px;line-height:37px;background:linear-gradient(#d3b676,#b8924e);color:var(--white);font-size:12px;border-radius:2px}
.thumb-round{top:1096px;width:198px;height:198px;border-radius:50%;border:6px solid #eeeeee;box-shadow:0 2px 6px rgba(0,0,0,.2)}

/* gallery */
.gallery{left:0;top:1615px;width:1200px;height:340px;background:var(--panel)}
.shot{top:1735px;width:186px;height:156px;border:5px solid var(--white);box-shadow:0 1px 4px rgba(0,0,0,.25)}
.side-arrow{color:#b5b5b5;font-size:34px;font-family:Arial,sans-serif;line-height:1}

/* reviews */
.review-box{left:97px;top:2078px;width:1003px;height:167px;background:#f4f4f4;border:1px solid #e3e3e3;padding:40px 40px 0}
.review-box p{font-size:12px;line-height:24px;color:#666;width:880px}
.stars{margin-top:16px;font-size:12px;color:#f08a24;display:flex;align-items:center;gap:12px}
.stars a{color:#2f7fb3;font-size:11px;text-decoration:none}

/* clients */
.clients{left:0;top:2310px;width:1200px;height:265px;background:var(--panel)}
.client{top:2425px;width:170px;height:95px;background:var(--white);box-shadow:0 1px 3px rgba(0,0,0,.15);display:flex;align-items:center;justify-content:center;font-family:"Open Sans",Arial,sans-serif;font-weight:600;font-size:16px;color:#3b3b3b;text-align:center}

/* footer */
.footer{left:0;top:2575px;width:1200px;height:265px;background:var(--footer)}
.footer-brand{left:100px;top:2650px;display:flex;align-items:center;gap:12px}
.footer-brand .brand-name{font-size:22px;line-height:24px}
.footer-brand .brand-mark{width:30px;height:30px}
.f-title{top:2612px;color:var(--white);font-family:"Cinzel",Georgia,serif;font-size:15px;letter-spacing:1px}
.f-links{left:330px;top:2645px;list-style:none;color:#e8e8e8;font-size:12px;line-height:27px}
.f-chat{left:548px;top:2646px;color:#e8e8e8;font-size:12px;line-height:20px}
.f-chat .row{display:flex;gap:14px;margin-bottom:18px}
.field{left:850px;width:250px;height:33px;border:1px solid #9a9a9a;background:#5e5e5e;color:#c9c9c9;font-size:11px;padding:8px 10px}
.submit{left:850px;top:2793px;width:88px;height:33px;background:var(--gold-btn);color:var(--white);font-size:12px;text-align:center;line-height:33px}
.footer-bar{left:0;top:2840px;width:1200px;height:63px;background:var(--footer-bar);color:#dcdcdc;font-size:11px}
.footer-bar .copy{left:100px;top:24px}
.footer-bar .connect{left:800px;top:24px;display:flex;align-items:center;gap:10px}
.footer-bar .dot{width:11px;height:11px;border-radius:50%;background:#dcdcdc;display:inline-block}
</style>
</head>
<body>

<header class="abs site-header">
  <div class="abs brand" style="left:100px;top:25px">
    <span class="brand-mark"></span>
    <span class="brand-name">Marlow Crest<br>Interiors</span>
  </div>
  <div class="abs social-top"><span></span><span></span><span></span><span></span><span></span></div>
  <nav class="abs main-nav"><span class="active">Home</span><span>Services</span><span>Gallery</span><span>Contact</span></nav>
</header>

<section class="abs hero" role="img" aria-label="Slideshow photo of a bright living room and kitchen with white cabinetry and wood floors"></section>
<svg class="abs hero-arrow" style="left:30px" width="20" height="44"><polyline points="16,2 4,22 16,42" fill="none" stroke="rgba(255,255,255,.6)" stroke-width="2"/></svg>
<svg class="abs hero-arrow" style="left:1150px" width="20" height="44"><polyline points="4,2 16,22 4,42" fill="none" stroke="rgba(255,255,255,.6)" stroke-width="2"/></svg>
<div class="abs hero-tag"><span class="sq"></span><span>South Florida<br>Interior Decor</span></div>

<h1 class="abs section-title" style="top:715px;font-weight:700">Welcome to Marlow Crest Interiors</h1>
<p class="abs welcome-text">From condos to estates, we can help you achieve the style you want.Have your house professionally decorated for a quicker sale.Decor outdated? Need new flooring or kitchen cabinets? We can help you.From condos to estates, we can help you achieve the style you want.Have your house professionally decorated for a quicker sale.Decor outdated? Need new flooring or kitchen cabinets? We can help you.From condos to estates, we can help you achieve the style you want.Have your house professionally decorated for a quicker saleFrom condos to estates, we can help you achieve the style you want.Have your house professionally decorated for a quicker sale.Decor outdated? Need new flooring or kitchen cabinets? We can help you.</p>

<section class="abs services" role="img" aria-label="Faded background photo of a modern home interior"></section>
<h2 class="abs section-title" style="top:1012px">Design Services</h2>

<article class="abs card" style="left:103px">
  <h3>Interior Decor</h3>
  <p>We are here to help you achieve the look you have been dreaming of. Interior Design packages start as low as $750 per room. Hourly Interior Design consultation available at $125/hr.</p>
  <span class="btn">Read More</span>
</article>
<article class="abs card" style="left:448px">
  <h3>Home Staging</h3>
  <p>Let us help you with the sale of your residence. Home Staging will make your house more appealing to buyers, accelerating the sale process and many times resulting in a price increase. We can stage your house with your current furniture (Staging Packages start at $950) or if the house is empty, we can furnish it for a low monthly price until it's sold.</p>
  <span class="btn">Read More</span>
</article>
<article class="abs card" style="left:793px">
  <h3>Restyle &amp; Redesign</h3>
  <p>Is your current decor outdated? Do you need help with new countertops, cabinetry or flooring? Whether you need to update the decor style, a quick refresh or have remodeling plans, we can help you with the process. Call us for a detailed quote.</p>
  <span class="btn">Read More</span>
</article>
<div class="abs thumb-round" style="left:156px;background:radial-gradient(#f3efe6,#b9a27c 60%,#5f7a45)" role="img" aria-label="Photo of an airy room with a sculptural staircase and plants"></div>
<div class="abs thumb-round" style="left:501px;background:radial-gradient(#e8e2d4,#9a7a52 60%,#5a6f48)" role="img" aria-label="Photo of a staged sitting area with a leather chair"></div>
<div class="abs thumb-round" style="left:846px;background:radial-gradient(#f1e6dc,#c98f6c 55%,#8a5a44)" role="img" aria-label="Photo of a design consultation in progress"></div>

<section class="abs gallery"></section>
<h2 class="abs section-title" style="top:1670px">Our Gallery</h2>
<span class="abs side-arrow" style="left:42px;top:1795px">&#8249;</span>
<span class="abs side-arrow" style="left:1138px;top:1795px">&#8250;</span>
<div class="abs shot" style="left:97px;background:linear-gradient(#dfe6e8,#c89a4a 70%,#e8e8e8)" role="img" aria-label="Gallery photo of a living room with orange accents"></div>
<div class="abs shot" style="left:302px;background:linear-gradient(#e6e4df,#7a6a58 70%,#4f5a3e)" role="img" aria-label="Gallery photo of a console table with plants"></div>
<div class="abs shot" style="left:507px;background:linear-gradient(#d9d3c5,#6e5640 70%,#3f4a39)" role="img" aria-label="Gallery photo of a dining room with chandelier"></div>
<div class="abs shot" style="left:712px;background:linear-gradient(#f0e6e4,#d9b7b8 60%,#c8c29a)" role="img" aria-label="Gallery photo of a bedroom in soft pink tones"></div>
<div class="abs shot" style="left:917px;background:linear-gradient(#d7b27a,#8a3a2e 60%,#5a3a2a)" role="img" aria-label="Gallery photo of a warm living room with red sofas"></div>

<h2 class="abs section-title" style="top:2010px">Our Dwellr Reviews</h2>
<div class="abs review-box">
  <p>From condos to estates, we can help you achieve the style you want.Have your house professionally decorated for a quicker sale.Decor outdated? Need new flooring or kitchen cabinets? We can help you.From condos to estates, we can help you achieve the style you want...</p>
  <div class="stars"><span>&#9733;&#9733;&#9733;&#9733;&#9734;</span><a>645 Reviews</a></div>
  <svg class="abs" style="left:947px;top:123px" width="30" height="14"><circle cx="6" cy="7" r="6" fill="#bbb"/><circle cx="21" cy="7" r="6" fill="#999"/><polyline points="8,4 5,7 8,10" fill="none" stroke="#fff" stroke-width="1.5"/><polyline points="19,4 22,7 19,10" fill="none" stroke="#fff" stroke-width="1.5"/></svg>
</div>

<section class="abs clients"></section>
<h2 class="abs section-title" style="top:2355px">Companies Logos Features as Clients</h2>
<span class="abs side-arrow" style="left:42px;top:2455px">&#8249;</span>
<span class="abs side-arrow" style="left:1138px;top:2455px">&#8250;</span>
<div class="abs client" style="left:103px">VORNA</div>
<div class="abs client" style="left:308px">Nest Wares</div>
<div class="abs client" style="left:513px">Durrandel</div>
<div class="abs client" style="left:718px">Tobias Quill</div>
<div class="abs client" style="left:925px">Plaza Furnishings</div>

<footer class="abs footer"></footer>
<div class="abs footer-brand"><span class="brand-mark"></span><span class="brand-name">Marlow Crest<br>Interiors</span></div>
<h4 class="abs f-title" style="left:330px">Quicklinks</h4>
<ul class="abs f-links"><li>&#8250; Home</li><li>&#8250; Services</li><li>&#8250; Gallery</li><li>&#8250; Contact</li></ul>
<h4 class="abs f-title" style="left:543px">Let's Chat!</h4>
<div class="abs f-chat">
  <div class="row">
    <svg width="14" height="12" style="margin-top:4px"><rect x="0.5" y="0.5" width="13" height="10" fill="#e8e8e8"/><polyline points="1,1 7,6 13,1" fill="none" stroke="#585858" stroke-width="1.2"/></svg>
    <span>Email:<br>hello@marlowcrestinteriors.example</span>
  </div>
  <div class="row">
    <svg width="14" height="14" style="margin-top:3px"><path d="M3 1 L5.5 1 L6.5 4.5 L4.8 5.8 Q6.2 8.6 8.2 9.2 L9.5 7.5 L13 8.5 L13 11 Q12 13 9.5 12.5 Q2.5 10 1.5 3.5 Q1.5 1.5 3 1Z" fill="#e8e8e8"/></svg>
    <span>Phone: +1 555 014 2248</span>
  </div>
</div>
<h4 class="abs f-title" style="left:850px">Contact Details</h4>
<div class="abs field" style="top:2652px">Enter your name</div>
<div class="abs field" style="top:2692px">Email address</div>
<div class="abs field" style="top:2732px;height:55px">Enter your massage</div>
<div class="abs submit">Submit</div>

<div class="abs footer-bar">
  <span class="abs copy">&copy; marlowcrestinteriors.example 2016. All rights reserved</span>
  <span class="abs connect">Connct with our social network : <i class="dot"></i><i class="dot"></i><i class="dot"></i><i class="dot"></i><i class="dot"></i></span>
  <span class="abs" style="left:1078px;top:24px">C12</span>
</div>

</body>
</html>
```